KTR Motorhaus Automotive Repair and Service Shop

I need an informative and interactive website for my automotive service and repair shop. The website must give information about the shop, as well as the ability to make bookings and a forums page for our users to use and set up an account with us, in which we can give promotions via email. We are located in Pompano Beach Florida and our company name is KTR Motorhaus. Our color scheme is a red for accent and grey (neutral color) as a base. The design must communicate our message and be able to grow should we decide to retail parts in the future. One of the websites I take the highest inspiration from is http://www.lanvexbodyshop.example/. Although I do not have as nearly as many certifications as them. Attached are some images of our shop so you can see how clean and modern our building is, and I would like our website to match our feel. Thank you.

Target Market(s)

Automotive Enthusiasts

Industry/Entity Type

Automotive

Contact Information for Business Card

KTR Motorhaus /954 718 6402 /rohan@ktrmotorhaus.example/ 512 NE 9th St Pompano Beach FL 33062/ any other info needed please ask me

Coding

Coded - Design and coding required

Number of Pages Required

5+ page

Font styles to use
Sans Serif

Requirements
Must have
• Name, logo, contact info, location, phone number
Nice to have
• Building is very modern, would like a business card to match
Should not have
• Not to playful or vibrant

```html
<!DOCTYPE html>
<html lang="en">
<head>
<meta charset="utf-8">
<title>KTR Motorhaus</title>
<link href="https://fonts.googleapis.com/css2?family=Poppins:wght@300;400;500;600;700&display=swap" rel="stylesheet">
<style>
:root{
  --red:#e81c2e;
  --red-dark:#a50f1c;
  --ink:#111111;
  --text:#333333;
  --muted:#8a8a8a;
  --light:#f4f4f4;
  --line:#d8d8d8;
  --white:#ffffff;
  --stage:#ececec;
}
*{box-sizing:border-box;margin:0;padding:0}
html,body{width:1200px;height:2485px;overflow:hidden;background:var(--stage);font-family:'Poppins',sans-serif;color:var(--text)}
.stage{width:1244px;height:2576px;transform:scale(.96463);transform-origin:0 0;position:relative}
.page{position:absolute;left:256px;top:69px;width:731px;height:2401px;background:var(--white);box-shadow:0 10px 40px rgba(0,0,0,.25);overflow:hidden}
.page *{position:absolute}
.page .flow,.page .flow *{position:static}
.btn{background:var(--red);color:var(--white);border-radius:20px;display:flex;align-items:center;justify-content:center;font-weight:500}
/* nav */
.nav{left:0;top:0;width:731px;height:50px;background:var(--red)}
.brand{left:90px;top:17px;color:var(--white);font-size:11px;font-weight:400}
.menu-item{top:0;height:50px;display:flex;align-items:center;color:var(--white);font-size:6.6px;font-weight:500;letter-spacing:.2px}
.menu-item.active{background:var(--ink);padding:0 11px}
.nav-cta{left:573px;top:14px;width:72px;height:21px;background:var(--white);color:var(--red);border-radius:12px;font-size:7px;display:flex;align-items:center;justify-content:center}
/* hero */
.hero{left:0;top:50px;width:731px;height:320px;background:radial-gradient(ellipse at 75% 60%,#5a0e14 0%,#2a2a2d 40%,#141416 80%)}
.hero-kicker{left:0;width:731px;top:86px;text-align:center;color:var(--red);font-size:13px;font-weight:300}
.hero-title{left:0;width:731px;top:106px;text-align:center;color:var(--white);font-size:34px;font-weight:700}
.hero-copy{left:150px;width:431px;top:157px;text-align:center;color:var(--white);font-size:8.2px;line-height:11.5px}
.hero-btn{left:319px;top:205px;width:91px;height:25px;font-size:9.5px}
/* about */
.about{left:0;top:370px;width:731px;height:280px;background:var(--light)}
.h2{font-size:15.5px;font-weight:500;color:var(--ink)}
.about-title{left:90px;top:60px}
.about-copy{left:90px;top:82px;width:220px;font-size:5.6px;line-height:9.9px;color:var(--muted)}
.about-btn{left:90px;top:198px;width:51px;height:16px;font-size:5.5px}
.about-photo{left:373px;top:41px;width:272px;height:198px;background:radial-gradient(ellipse at 45% 35%,#d7dde3 0%,#6c7680 35%,#1c2228 75%)}
/* services */
.services-title{left:0;width:731px;top:686px;text-align:center}
.service-card{top:722px;width:130px;height:156px;display:flex;align-items:center;justify-content:center;text-align:center;color:var(--white);font-size:11px;font-weight:600;line-height:12px}
.services-btn{left:312px;top:905px;width:105px;height:24px;font-size:8.5px}
/* reviews */
.reviews{left:0;top:970px;width:731px;height:179px;background:linear-gradient(180deg,#c6111f 0%,var(--red) 55%,#d3141f 100%)}
.reviews-title{left:0;width:731px;top:36px;text-align:center;color:var(--white);font-size:15.5px;font-weight:600}
.quote-mark{top:78px;color:var(--white);font-size:44px;font-weight:700;line-height:44px}
.review-copy{top:88px;width:207px;color:var(--white);font-size:5.3px;line-height:7.8px;text-align:justify}
.review-name{top:131px;color:var(--white);font-size:7.5px;font-weight:600}
.review-name span{position:static;color:#ffd400;letter-spacing:1px;font-size:6.5px;margin-left:3px}
.arrow{top:99px}
/* gallery */
.gallery-title{left:0;width:731px;top:1186px;text-align:center}
.photo{width:177px;height:177px}
.photo.a{background:radial-gradient(ellipse at 40% 55%,#b3121d 0%,#4a0a0e 45%,#121212 85%)}
.photo.b{background:radial-gradient(ellipse at 50% 45%,#b27a2c 0%,#3d3a36 45%,#1c1c1c 90%)}
.photo.c{background:radial-gradient(ellipse at 55% 65%,#c41a22 0%,#8a8580 45%,#3b3937 90%)}
.gallery-btn{left:312px;top:1618px;width:105px;height:24px;font-size:8.5px}
/* certified */
.certified{left:0;top:1683px;width:731px;height:215px;background:var(--light)}
.cert-title{left:0;width:731px;top:33px;text-align:center}
.cert-copy{left:155px;width:421px;top:59px;text-align:center;font-size:6.3px;line-height:9.2px;color:var(--muted)}
.badge{top:108px;width:67px;height:66px;background:var(--white);border:1px solid var(--line);display:flex;align-items:center;justify-content:center}
.badge i{position:static;display:block;width:44px;height:44px;border-radius:50%;background:#9a9ea4}
/* contact */
.map{left:77px;top:1938px;width:272px;height:230px;background:linear-gradient(135deg,#eceae6,#dcdad6)}
.contact-title{left:409px;top:1933px}
.field-label{font-size:5.3px;color:var(--ink)}
.field{width:105px;height:16px;border:1px solid var(--line);font-size:4.8px;color:#aaa;padding:5px 8px}
.message{left:409px;top:2077px;width:236px;height:56px;border:1px solid var(--line);font-size:4.8px;color:#aaa;padding:6px 8px}
.submit-btn{left:409px;top:2145px;width:85px;height:23px;font-size:7px}
/* footer */
.footer{left:0;top:2209px;width:731px;height:165px;background:radial-gradient(ellipse at 60% 40%,#6b0f17 0%,#2a0a0d 45%,#120909 85%)}
.foot-head{top:44px;color:var(--white);font-size:8.5px;font-weight:400}
.foot-link{color:var(--white);font-size:5.5px}
.foot-info{color:var(--white);font-size:5.3px;line-height:8.5px;display:flex;gap:5px}
.social{top:68px;width:14px;height:14px;background:var(--red);border-radius:2px}
.search{left:514px;top:94px;width:112px;height:13px;background:var(--white);border-radius:8px;font-size:4.8px;color:#aaa;padding:3px 8px}
.copyright{left:0;top:2374px;width:731px;height:27px;background:var(--red);color:var(--white);font-size:5.3px;display:flex;align-items:center;justify-content:center}
</style>
</head>
<body>
<div class="stage">
<div class="page">

  <header class="nav">
    <div class="brand">KTR Motorhaus</div>
    <div class="menu-item active" style="left:197px">HOME</div>
    <div class="menu-item" style="left:251px">ABOUT US</div>
    <div class="menu-item" style="left:309px">OUR SERVICES</div>
    <div class="menu-item" style="left:383px">GALLERY</div>
    <div class="menu-item" style="left:440px">BLOGS</div>
    <div class="menu-item" style="left:487px">CONTACT US</div>
    <div class="nav-cta">Contact Us</div>
  </header>

  <section class="hero" role="img" aria-label="Dark workshop photo with stacked tyres and a red sports car">
    <div class="hero-kicker">MODERN EQUIPMENT</div>
    <h1 class="hero-title">Quailty Service for You</h1>
    <p class="hero-copy">Lorem Ipsum is simply dummy text of the printing and typesetting industry. Lorem Ipsum has been the industry's standard dummy text ever since the 1500s, when an unknown printer took a galley of type and scrambled it to make a type specimen book.</p>
    <div class="btn hero-btn">Contact Us</div>
  </section>

  <section class="about">
    <h2 class="h2 about-title">About Us</h2>
    <div class="about-copy">
      <p class="flow">Lorem Ipsum is simply dummy text of the printing and typesetting industry. Lorem Ipsum has been the industry's standard dummy text ever since the 1500s, when an unknown printer took a galley of type and scrambled it to make a type specimen book. It has survived not only five centuries, but also the leap into electronic typesetting, remaining essentially unchanged.</p>
      <p class="flow" style="margin-top:10px">It was popularised in the 1960s with the release of Presstype sheets containing Lorem Ipsum passages, and more recently with desktop publishing software like PageForge Studio.</p>
    </div>
    <div class="btn about-btn">Read More</div>
    <div class="about-photo" role="img" aria-label="Red sports car speeding through a lit tunnel"></div>
  </section>

  <h2 class="h2 services-title">Our Services</h2>
  <div class="service-card" style="left:90px;background:linear-gradient(160deg,#4a4d52,#1d1f22)" role="img" aria-label="Technician working under a car bonnet">Collision<br>Repair</div>
  <div class="service-card" style="left:231px;background:linear-gradient(160deg,#8c7f70,#3a3a3f)" role="img" aria-label="Worker applying protective film to a car">Paint<br>Protection</div>
  <div class="service-card" style="left:373px;background:linear-gradient(160deg,#55595e,#24272b)" role="img" aria-label="Modified sports car front view">Customization<br>Upgrades</div>
  <div class="service-card" style="left:515px;background:linear-gradient(160deg,#3d3f43,#141517)" role="img" aria-label="Hands repairing a dent with a tool">Paintless<br>Dent Removal</div>
  <div class="btn services-btn">See All Services</div>

  <section class="reviews" role="img" aria-label="Red tinted sports car background">
    <h2 class="reviews-title">Clients Reviews</h2>
    <svg class="arrow" style="left:51px" width="8" height="14" viewBox="0 0 8 14"><path d="M7 1 1 7l6 6" fill="none" stroke="#fff" stroke-width="1.3"/></svg>
    <svg class="arrow" style="left:676px" width="8" height="14" viewBox="0 0 8 14"><path d="M1 1l6 6-6 6" fill="none" stroke="#fff" stroke-width="1.3"/></svg>
    <div class="quote-mark" style="left:95px">&ldquo;</div>
    <p class="review-copy" style="left:143px">Lorem Ipsum is simply dummy text of the printing and typesetting industry. Lorem Ipsum has been the industry's standard dummy text ever since the 1500s, when an unknown printer took a galley of type and scrambled it to make a type specimen book. It has survived not only five centuries, but also the leap into electronic typesetting, remaining essentially unchanged.</p>
    <div class="review-name" style="left:143px">John Doe <span>★★★★★</span></div>
    <div class="quote-mark" style="left:378px">&ldquo;</div>
    <p class="review-copy" style="left:425px">Lorem Ipsum is simply dummy text of the printing and typesetting industry. Lorem Ipsum has been the industry's standard dummy text ever since the 1500s, when an unknown printer took a galley of type and scrambled it to make a type specimen book. It has survived not only five centuries, but also the leap into electronic typesetting, remaining essentially unchanged.</p>
    <div class="review-name" style="left:425px">John Doe <span>★★★★★</span></div>
  </section>

  <h2 class="h2 gallery-title">Photo Gallery</h2>
  <div class="photo a" style="left:90px;top:1224px" role="img" aria-label="Front of a red sports car in a dark garage"></div>
  <div class="photo b" style="left:279px;top:1224px" role="img" aria-label="Exposed engine of a sports car in a workshop"></div>
  <div class="photo c" style="left:467px;top:1224px" role="img" aria-label="Red classic roadster with open bonnet in a garage"></div>
  <div class="photo a" style="left:90px;top:1412px" role="img" aria-label="Front of a red sports car in a dark garage"></div>
  <div class="photo b" style="left:279px;top:1412px" role="img" aria-label="Exposed engine of a sports car in a workshop"></div>
  <div class="photo c" style="left:467px;top:1412px" role="img" aria-label="Red classic roadster with open bonnet in a garage"></div>
  <div class="btn gallery-btn">See All Photos</div>

  <section class="certified">
    <h2 class="h2 cert-title">Certified Repair Facility</h2>
    <p class="cert-copy">We provide highly trained technicians that are TechCert and AutoSkill certified to ensure your repair or project matches or exceeds industry standards. In addition to their credentials and certifications, our technicians' deep experience and tenure with the Company is unparalleled in the South Florida market and beyond.</p>
    <div class="badge" style="left:95px"><i></i></div>
    <div class="badge" style="left:189px"><i></i></div>
    <div class="badge" style="left:283px"><i></i></div>
    <div class="badge" style="left:378px"><i></i></div>
    <div class="badge" style="left:472px"><i></i></div>
    <div class="badge" style="left:567px"><i></i></div>
  </section>

  <div class="map" role="img" aria-label="Street map showing the shop location"></div>
  <h2 class="h2 contact-title">Contact Us</h2>
  <div class="field-label" style="left:409px;top:1966px">First Name:</div>
  <div class="field" style="left:409px;top:1976px">John Doe</div>
  <div class="field-label" style="left:540px;top:1966px">Last Name:</div>
  <div class="field" style="left:540px;top:1976px">John Doe</div>
  <div class="field-label" style="left:409px;top:2000px">Phone Number:</div>
  <div class="field" style="left:409px;top:2010px">+1 234 234 4683</div>
  <div class="field-label" style="left:540px;top:2000px">Email:</div>
  <div class="field" style="left:540px;top:2010px">John Doe</div>
  <div class="field-label" style="left:409px;top:2034px">Car Year, Make &amp; Model:</div>
  <div class="field" style="left:409px;top:2043px">John Doe</div>
  <div class="field-label" style="left:540px;top:2034px">Service Requested:</div>
  <div class="field" style="left:540px;top:2043px">John Doe</div>
  <div class="field-label" style="left:409px;top:2067px">Message</div>
  <div class="message">Typing...</div>
  <div class="btn submit-btn">Submit Message</div>

  <footer class="footer" role="img" aria-label="Dark red tinted sports car background">
    <div class="foot-head" style="left:90px">QUICK LINKS</div>
    <div style="left:90px;top:59px;display:flex;flex-direction:column;gap:7.5px">
      <span class="flow foot-link">Our History</span><span class="flow foot-link">Services</span><span class="flow foot-link">Gallery</span><span class="flow foot-link">Contact Us</span><span class="flow foot-link">Schedule Appointment</span>
    </div>
    <div class="foot-head" style="left:231px">ACCOUNT</div>
    <div style="left:231px;top:59px;display:flex;flex-direction:column;gap:7.5px">
      <span class="flow foot-link">Preference</span><span class="flow foot-link">Order history</span><span class="flow foot-link">Cart Page</span><span class="flow foot-link">Sign In</span>
    </div>
    <div class="foot-head" style="left:372px">CONTACT US</div>
    <div class="foot-info" style="left:372px;top:59px"><svg class="flow" width="5" height="7" viewBox="0 0 5 7"><path d="M2.5 0A2.5 2.5 0 0 0 0 2.5C0 4.3 2.5 7 2.5 7S5 4.3 5 2.5A2.5 2.5 0 0 0 2.5 0z" fill="#fff"/></svg><span class="flow">Harbor Works, 512 NE 9th St,<br>Pompano Beach FL</span></div>
    <div class="foot-info" style="left:372px;top:84px"><svg class="flow" width="5" height="6" viewBox="0 0 5 6"><path d="M1 0 0 1c0 2.5 1.5 5 4 5l1-1-1.3-1.2-.8.5C2 3.7 1.3 3 .9 2.1l.5-.8z" fill="#fff"/></svg><span class="flow">1-800-555-0148</span></div>
    <div class="foot-info" style="left:372px;top:100px"><svg class="flow" width="6" height="5" viewBox="0 0 6 5"><rect width="6" height="5" fill="#fff"/><path d="M0 0l3 2.5L6 0" fill="none" stroke="#888" stroke-width=".6"/></svg><span class="flow">hello@ktrmotorhaus.example</span></div>
    <div class="foot-head" style="left:514px">GET IN TOUCH</div>
    <div class="social" style="left:514px"></div>
    <div class="social" style="left:535px"></div>
    <div class="social" style="left:557px"></div>
    <div class="social" style="left:578px"></div>
    <div class="search">Search...</div>
  </footer>
  <div class="copyright">© 2020 KTR Motorhaus. All rights reserved.</div>

</div>
</div>
</body>
</html>
```